Consulting company needs Business Cards - rough concept provided

I'm looking for someone to take our business card idea and make is slick and polished - to communicate our high-end, sophisticated, serious consulting business. We have a rough layout we did in-house. We are open to ideas on repo-ing elements, adjusting sizes, typefaces etc... within the general concept we've already come up with. We want it to be super-clean and sophisticated. We want to keep the white backgrounds, and blue brand colors. Our goal is to print with painted blue edges on thick cardstock. Thank you!!

```html
<!DOCTYPE html>
<html lang="en">
<head>
<meta charset="utf-8">
<title>Lumenridge Business Card</title>
<link rel="stylesheet" href="https://fonts.googleapis.com/css2?family=Inter:wght@300;400;500;700;800&display=swap">
<style>
  :root {
    --brand-blue: #0a82c8;
    --rule-blue: #7cc0e6;
    --ink: #111111;
    --ink-soft: #2a2a2a;
    --paper: #ffffff;
    --icon-line: #555555;
  }
  * { margin: 0; padding: 0; box-sizing: border-box; }
  html, body {
    width: 1200px;
    height: 703px;
    overflow: hidden;
    background: var(--paper);
  }
  .business-card {
    position: relative;
    width: 1200px;
    height: 703px;
    background: var(--paper);
    font-family: "Inter", Arial, sans-serif;
    color: var(--ink);
  }
  .company-name {
    position: absolute;
    left: 100px;
    top: 88px;
    width: 1000px;
    font-size: 138px;
    font-weight: 800;
    line-height: 1;
    letter-spacing: -3px;
    color: var(--brand-blue);
    text-align: center;
  }
  .brand-rule {
    position: absolute;
    left: 100px;
    top: 290px;
    width: 1000px;
    height: 2px;
    background: var(--rule-blue);
  }
  .person {
    position: absolute;
    left: 380px;
    top: 330px;
  }
  .person-name {
    font-size: 44px;
    font-weight: 700;
    letter-spacing: 2px;
    line-height: 1.1;
  }
  .person-title {
    margin-top: 6px;
    margin-left: 8px;
    font-size: 34px;
    font-weight: 300;
    letter-spacing: 1.5px;
    color: var(--ink-soft);
  }
  .contact-list {
    position: absolute;
    left: 370px;
    top: 478px;
    list-style: none;
  }
  .contact-item {
    display: flex;
    align-items: flex-start;
    gap: 22px;
    font-size: 24px;
    font-weight: 400;
    letter-spacing: 1.5px;
    line-height: 34px;
    margin-bottom: 6px;
  }
  .contact-icon {
    width: 32px;
    height: 32px;
    flex: none;
    margin-top: 2px;
    fill: none;
    stroke: var(--icon-line);
    stroke-width: 1.4;
  }
</style>
</head>
<body>
  <main class="business-card">
    <div class="company-name">LUMENRIDGE</div>
    <div class="brand-rule"></div>

    <section class="person">
      <h1 class="person-name">DANA WHITFIELD</h1>
      <p class="person-title">BRAND CONSULTANT</p>
    </section>

    <ul class="contact-list">
      <li class="contact-item">
        <svg class="contact-icon" viewBox="0 0 32 32" aria-hidden="true">
          <path d="M16 29 C10 21 7 16 7 12 a9 9 0 0 1 18 0 c0 4 -3 9 -9 17z"/>
          <circle cx="16" cy="12" r="3.5"/>
        </svg>
        <span>4830 HARBOR RIDGE BLVD, STE 210<br>WESTBROOK, CA 90377</span>
      </li>
      <li class="contact-item">
        <svg class="contact-icon" viewBox="0 0 32 32" aria-hidden="true">
          <path d="M8 5 l5 0 l2 7 l-3 3 c2 4 4 6 8 8 l3 -3 l7 2 l0 5 c-12 1 -23 -10 -22 -22z"/>
        </svg>
        <span>(555) 310 4872</span>
      </li>
      <li class="contact-item">
        <svg class="contact-icon" viewBox="0 0 32 32" aria-hidden="true">
          <rect x="3" y="8" width="26" height="17"/>
          <path d="M3 8 l13 10 l13 -10 M3 25 l10 -9 M29 25 l-10 -9"/>
        </svg>
        <span>DANA@LUMENRIDGE.COM</span>
      </li>
    </ul>
  </main>
</body>
</html>
```